Flyer for "Learn to Brew Craft Beer" course

NEEDED: A6 flyer designed to advertise my first training course:
Intro to craft beer brewing

The company brand identity was recently bought from Pixel Harbour and it can be seen, with colour scheme on our website: www.TallowMashworks.com.

The flyer is to be in line with my current brand identity and have a strong hook to push people to our site.

The flyer's goal is to get people to visit the site to book on a craft beer brewing training course. The info available to be included, although you have the freedom to include as much or as little as you see fit:

Currently a sale of 60% off on the course cost
RRP £120 Sale Price £50 (limited time only)
Courses will be run in central London
The website is TallowMashworks.com
Hands on, half day course, brunch and a couple of sample beers included
Dates available:
14th December 2014
11th January 2015
18th January 2015
25th January 2015
1st February 2015
8th February 2015
15th February 2015
22nd February 2015

Logo file included, AI version available on request. Any photo on the TallowMashworks.com site is available to be used. Simply pull of the site or I can send to you.

Colour scheme used on site: #FF9700 & #26210D

I will reply to any designs offered between 8pm and 11pm BST each day.

Good luch!

Hi everyone, We have now reviewed the first submissions and there are some ok, some good and a couple of great efforts in there. Here are the following common things that we commented on in our first reviews: 1. WHAT IS THE FLYER TRYING TO SAY... YOU'VE GOT 1 SECOND!!!! This flyer is to be given out in the street. That gives you 1second to tell the reader what the flyer is selling. That is the number 1 priority for the flyer. Please make it your priority as designers. 2. SALE SALE SALE This is the number 2 priority, people love SALES and a big colourful sticker saying SALE or 60% OFF (or both) is to be positioned so once the reader has seen that the flyer is about a craft beer brewing course, they see there is a sale on the course. 3. BRAND PERSONALITY 3rd priority is the Tallow Mashworks brand identity. We picked this name, logo and colour scheme to stand out. Please use these to enhance points 1 & 2, but also get our logo on there is a bold and brash way. 4. USE THE BACK OF THE CARD Place any info that is not required in 1, 2 & 3 on the back, or even remove it all together if YOU feel it is not suited. You are the designer, so make some design decisions! We are happy to ask you to add things back in if we feel it is lacking. Our best guess (and we are NOT designers) is that putting either the dates OR a brief description of the course on the back would be enough info. If you think we can get bother, without overloading the page, give it a go! 5. CALL TO ACTION On the front and on the back, we want a CALL TO ACTION. Book at TallowMashworks.com or just TallowMashworks.com (you do not need http://www before it!!! We live in 2014 not 1994!!!) 6. MAKE IT BOLD, & THEN MAKE IT BOLDER This flyer is to stand out to a person that is handed 1 different leaflet every 2 minutes while walking down a busy London high street. We MUST stand out. Finally, thanks for all the designer so far, your efforts are greatly appreciated and we are very excited about the new revision of the design!

Target Market(s)

City living, young professionals who like to do fun things at the weekend.

Industry/Entity Type

Training

Font styles to use
Sans Serif

Colors
f78f20

Requirements
Must have
• Strong brand identity and call to action
In line with brand identity, see website www.TallowMashworks.com

```html
<!DOCTYPE html>
<html lang="en">
<head>
<meta charset="utf-8">
<title>Tallow Mashworks – Craft Beer Brewing Course Flyer</title>
<link rel="stylesheet" href="https://fonts.googleapis.com/css2?family=Open+Sans:wght@400;700;800&family=Quicksand:wght@300;400&family=Yellowtail&family=Righteous&display=swap">
<style>
  :root {
    --stage: #e9e5de;
    --shield: #2b281d;
    --shield-edge: #3a3627;
    --band: #332f22;
    --orange: #f7941d;
    --sky: #a8d6ef;
    --white: #ffffff;
    --taps-a: #c9a273;
    --taps-b: #6e4a2a;
    --barrel-a: #1a110b;
    --barrel-b: #7a4a1e;
    --brewery-a: #b7aa97;
    --brewery-b: #5d564a;
    --table-a: #d9b98f;
    --table-b: #8a6a45;
  }
  * { margin: 0; padding: 0; box-sizing: border-box; }
  html, body { width: 1200px; height: 907px; overflow: hidden; background: var(--stage); }
  .flyer {
    position: absolute; left: 63px; top: 75px; width: 1072px; height: 760px;
    overflow: hidden; font-family: "Open Sans", sans-serif; color: var(--white);
  }
  .photo { position: absolute; }
  .photo--brewery { left: 433px; top: 0; width: 639px; height: 760px;
    background: linear-gradient(135deg, var(--brewery-a), var(--brewery-b) 70%, #3f3a32); }
  .photo--taps { left: 0; top: 0; width: 433px; height: 397px;
    background: radial-gradient(ellipse at 45% 55%, var(--taps-a), var(--taps-b) 80%); }
  .photo--barrels { left: 0; top: 397px; width: 433px; height: 363px;
    background: radial-gradient(ellipse at 60% 35%, var(--barrel-b), var(--barrel-a) 75%); }
  .photo--table { left: 727px; top: 320px; width: 345px; height: 440px;
    background: linear-gradient(180deg, #a89a86 0%, var(--table-a) 60%, var(--table-b) 100%); }
  .shield { position: absolute; left: 0; top: 0; }
  .brand-mark { position: absolute; left: 0; width: 100%; top: 70px; text-align: center; }
  .brand-mark__inner { position: absolute; left: 562px; top: 48px; transform: translateX(-50%);
    display: flex; flex-direction: column; align-items: center; gap: 10px; }
  .brand-mark__dot { width: 44px; height: 44px; border-radius: 50%; background: var(--white); }
  .brand-mark__name { font-weight: 800; font-size: 17px; letter-spacing: 2px; text-transform: uppercase; white-space: nowrap; }
  .text { position: absolute; white-space: nowrap; }
  .headline { left: 287px; width: 785px; top: 212px; text-align: center; font-weight: 700; font-size: 57px; letter-spacing: 1px; line-height: 1; }
  .lead { left: 397px; width: 540px; top: 307px; text-align: center; font-family: "Quicksand", sans-serif; font-weight: 400; font-size: 30px; color: var(--orange); }
  .course-name { left: 397px; width: 540px; top: 340px; text-align: center; font-family: "Yellowtail", cursive; font-size: 52px; color: var(--sky); }
  .details { left: 397px; width: 540px; top: 415px; text-align: center; font-family: "Quicksand", sans-serif; font-size: 19px; font-variant: small-caps; line-height: 34px; letter-spacing: 1px; }
  .details em { font-family: "Yellowtail", cursive; font-style: normal; color: var(--orange); font-size: 30px; }
  .location { right: 365px; top: 502px; text-align: right; font-weight: 700; line-height: 1; }
  .location__lead { font-size: 36px; color: var(--orange); letter-spacing: 1px; }
  .location__mid { font-size: 21px; color: var(--orange); margin-top: 4px; }
  .location__city { font-size: 21px; color: var(--sky); margin-top: 5px; }
  .sale { left: 724px; top: 488px; font-family: "Righteous", sans-serif; line-height: 1; }
  .sale__word { font-size: 55px; color: var(--orange); letter-spacing: 1px; }
  .sale__figure { font-size: 78px; color: var(--sky); margin-top: -6px; display: inline-block; }
  .sale__off { position: absolute; left: 162px; top: 62px; transform: rotate(90deg); transform-origin: left top;
    font-size: 19px; color: var(--orange); left: 185px; }
  .sale__cost { font-size: 18px; color: var(--orange); letter-spacing: 2px; word-spacing: 12px; margin-top: -4px; }
  .call-to-action { left: 397px; width: 540px; top: 634px; text-align: center; font-weight: 700; font-size: 25px; }
</style>
</head>
<body>
<main class="flyer">
  <div class="photo photo--brewery" role="img" aria-label="Blurred brewery interior with steel brewing equipment"></div>
  <div class="photo photo--taps" role="img" aria-label="Bar counter with beer taps and bottles in an ice bucket"></div>
  <div class="photo photo--barrels" role="img" aria-label="Stacked oak beer barrels in a dim cellar"></div>
  <div class="photo photo--table" role="img" aria-label="Wooden tabletop with a soft blurred background"></div>

  <svg class="shield" width="1072" height="760" viewBox="0 0 1072 760">
    <path d="M397 40 L937 40 Q905 110 930 200 Q960 330 960 420 Q955 560 900 620 Q760 700 667 725 Q574 700 434 620 Q379 560 374 420 Q374 330 404 200 Q429 110 397 40 Z"
          fill="var(--shield)" fill-opacity="0.93" stroke="var(--shield-edge)" stroke-width="2"/>
    <rect x="287" y="207" width="785" height="63" fill="var(--band)" fill-opacity="0.95"/>
  </svg>

  <div class="brand-mark__inner">
    <span class="brand-mark__dot"></span>
    <span class="brand-mark__name">Tallow Mashworks</span>
  </div>

  <h1 class="text headline">TALLOW MASHWORKS</h1>
  <p class="text lead">BOOK A TRAINING COURSE ON A</p>
  <p class="text course-name">Craft Beer Brewing</p>
  <p class="text details">Hands on, half day course, brunch<br><em>&amp;</em> a couple of sample beers included</p>

  <div class="text location">
    <div class="location__lead">COURSES</div>
    <div class="location__mid">WILL BE RUN IN</div>
    <div class="location__city">CENTRAL LONDON</div>
  </div>

  <div class="text sale">
    <div class="sale__word">SALE</div>
    <div class="sale__figure">60%</div>
    <div class="sale__off">OFF</div>
    <div class="sale__cost">COURSE COST</div>
  </div>

  <p class="text call-to-action">TALLOWMASHWORKS.COM</p>
</main>
</body>
</html>
```